This is book 2 to Mirage Harbor. I'm looking for something that feels similar, with the same cymatic image used on Antarctica on the first book cover (see the cover image attached; the original designer said this was the image used: https://www.filevaultexample.net/share/8k2m4p7q9r1t/cymatic-image.png). Differences: the cover should be all black (no Antarctica, no globe, nothing but the image), the cymatic image kind of a pale grayish white (subtle, not calling too much attention to itself. Think the subtle dragon on "The Boy beneath the Copper Lantern"--like that sort of). Same font as before, but red this time (with the color progression like in the first one, only red instead of blue), with the title (Mirage Assault), author name (M.J. Holt), and subtitle (Dawn of the Velorathi, Book 2)

Target Market(s)

adult action/adventure and thriller readers

Industry/Entity Type

media and literature

Colors
EB3D1F
EC4F4E
F09395
F8D3D4
FCEDEE

Requirements
Must have
• look like part of the series before
Should not have
• not too busy

```html
<!DOCTYPE html>
<html lang="en">
<head>
<meta charset="utf-8">
<title>Mirage Assault — Book Cover</title>
<link rel="stylesheet" href="https://fonts.googleapis.com/css2?family=Saira+Extra+Condensed:wght@500&family=Cinzel:wght@500;600&display=swap">
<style>
  :root {
    --cover-black: #231f20;
    --cover-deep: #1a1718;
    --red-hot: #ec2a32;
    --red-mid: #f08060;
    --blush: #f8d3d4;
    --text-white: #ffffff;
    --star: #cfe0f0;
    --rule-red: #b8262c;
  }
  html, body {
    margin: 0;
    padding: 0;
    width: 873px;
    height: 1200px;
    overflow: hidden;
    background: var(--cover-black);
  }
  .cover {
    display: block;
    width: 873px;
    height: 1200px;
  }
  .title {
    font-family: "Saira Extra Condensed", "Arial Narrow", sans-serif;
    font-weight: 500;
    font-size: 250px;
    text-transform: uppercase;
  }
  .series-line {
    font-family: "Cinzel", "Times New Roman", serif;
    font-weight: 600;
    font-size: 32px;
    fill: var(--text-white);
  }
  .author {
    font-family: "Cinzel", "Times New Roman", serif;
    font-weight: 500;
    font-size: 64px;
    fill: var(--text-white);
  }
  .star { fill: var(--star); }
  .red-star { fill: #e0262d; opacity: 0.8; }
</style>
</head>
<body>
  <svg class="cover" viewBox="0 0 873 1200" xmlns="http://www.w3.org/2000/svg">
    <defs>
      <linearGradient id="bg-fade" x1="0" y1="0" x2="0" y2="1">
        <stop offset="0" stop-color="var(--cover-black)"/>
        <stop offset="1" stop-color="var(--cover-deep)"/>
      </linearGradient>
      <radialGradient id="top-glow" cx="0.5" cy="0" r="0.5" gradientTransform="translate(0 0) scale(1 0.3)">
        <stop offset="0" stop-color="#ec2a32" stop-opacity="0.95"/>
        <stop offset="0.55" stop-color="#ec2a32" stop-opacity="0.35"/>
        <stop offset="1" stop-color="#ec2a32" stop-opacity="0"/>
      </radialGradient>
      <linearGradient id="title-fade-down" gradientUnits="userSpaceOnUse" x1="0" y1="79" x2="0" y2="257">
        <stop offset="0" stop-color="var(--red-hot)"/>
        <stop offset="0.35" stop-color="var(--red-mid)"/>
        <stop offset="0.65" stop-color="var(--blush)"/>
        <stop offset="0.9" stop-color="var(--text-white)"/>
      </linearGradient>
      <linearGradient id="title-fade-up" gradientUnits="userSpaceOnUse" x1="0" y1="281" x2="0" y2="457">
        <stop offset="0.1" stop-color="var(--text-white)"/>
        <stop offset="0.35" stop-color="var(--blush)"/>
        <stop offset="0.65" stop-color="var(--red-mid)"/>
        <stop offset="0.9" stop-color="var(--red-hot)"/>
      </linearGradient>
      <linearGradient id="rule-fade" x1="0" y1="0" x2="1" y2="0">
        <stop offset="0" stop-color="var(--rule-red)" stop-opacity="0"/>
        <stop offset="0.15" stop-color="#8a1e22"/>
        <stop offset="0.5" stop-color="var(--rule-red)"/>
        <stop offset="0.85" stop-color="#8a1e22"/>
        <stop offset="1" stop-color="var(--rule-red)" stop-opacity="0"/>
      </linearGradient>
      <radialGradient id="cymatic-tone" cx="0.5" cy="0.5" r="0.5">
        <stop offset="0" stop-color="#2b2829"/>
        <stop offset="0.5" stop-color="#444142"/>
        <stop offset="0.8" stop-color="#6e6c6c"/>
        <stop offset="0.95" stop-color="#4a4748"/>
        <stop offset="1" stop-color="#231f20" stop-opacity="0"/>
      </radialGradient>
    </defs>

    <rect class="background" width="873" height="1200" fill="url(#bg-fade)"/>
    <rect class="glow" width="873" height="300" fill="url(#top-glow)"/>

    <g class="starfield" aria-hidden="true">
      <circle class="star" cx="40" cy="60" r="1.6"/><circle class="star" cx="200" cy="14" r="1.4"/><circle class="star" cx="355" cy="10" r="1.6"/>
      <circle class="star" cx="560" cy="30" r="1.3"/><circle class="star" cx="700" cy="52" r="1.8"/><circle class="star" cx="812" cy="90" r="1.5"/>
      <circle class="star" cx="25" cy="200" r="1.4"/><circle class="star" cx="850" cy="210" r="1.6"/><circle class="star" cx="60" cy="330" r="1.7"/>
      <circle class="star" cx="760" cy="370" r="1.8"/><circle class="star" cx="18" cy="420" r="1.5"/><circle class="star" cx="840" cy="450" r="1.4"/>
      <circle class="star" cx="80" cy="560" r="1.5"/><circle class="star" cx="800" cy="580" r="1.7"/><circle class="star" cx="30" cy="650" r="1.6"/>
      <circle class="star" cx="855" cy="680" r="1.4"/><circle class="star" cx="70" cy="760" r="1.5"/><circle class="star" cx="820" cy="800" r="1.7"/>
      <circle class="star" cx="22" cy="880" r="1.4"/><circle class="star" cx="790" cy="900" r="1.5"/><circle class="star" cx="60" cy="980" r="1.6"/>
      <circle class="star" cx="840" cy="1010" r="1.4"/><circle class="star" cx="50" cy="1080" r="1.5"/><circle class="star" cx="760" cy="1090" r="1.7"/>
      <circle class="star" cx="180" cy="1180" r="1.4"/><circle class="star" cx="420" cy="1188" r="1.5"/><circle class="star" cx="660" cy="1180" r="1.6"/>
      <circle class="star" cx="850" cy="1150" r="1.4"/><circle class="star" cx="300" cy="700" r="1.4"/><circle class="star" cx="560" cy="760" r="1.5"/>
      <circle class="red-star" cx="715" cy="42" r="3"/><circle class="red-star" cx="92" cy="860" r="3.5"/><circle class="red-star" cx="867" cy="276" r="3"/>
    </g>

    <text class="title" x="436.5" y="257" text-anchor="middle" textLength="560" lengthAdjust="spacingAndGlyphs" fill="url(#title-fade-down)">Mirage</text>
    <text class="title" x="436.5" y="457" text-anchor="middle" textLength="600" lengthAdjust="spacingAndGlyphs" fill="url(#title-fade-up)">Assault</text>

    <rect class="series-rule" x="50" y="478" width="810" height="2" fill="url(#rule-fade)"/>
    <text class="series-line" x="436.5" y="517" text-anchor="middle" textLength="660" lengthAdjust="spacingAndGlyphs">DAWN OF THE VELORATHI, BOOK 2</text>
    <rect class="series-rule" x="36" y="527" width="800" height="2" fill="url(#rule-fade)"/>

    <ellipse class="cymatic-art" role="img" aria-label="Subtle pale grey cymatic flower pattern on black" cx="434" cy="821" rx="332" ry="272" fill="url(#cymatic-tone)" opacity="0.8"/>

    <text class="author" x="436.5" y="1151" text-anchor="middle" textLength="433" lengthAdjust="spacingAndGlyphs">M.J. HOLT</text>
  </svg>
</body>
</html>
```